Box and Paper Bag Design
for exclusive line of prescriptions creams
Box and Paper Bag Design  - Health
Creative Brief
A design for the box (layout attached) and a promotional paper bag (no layout - see sample picture: 8" length, 7" high, 3.5" deep) - front and back designs will be fine. Both packages are for exclusive line of prescription creams. Should resemble expensive, high end, sophisticated and upscale style, yet THIS IS PRESCRIPTION MEDICATION - the packaging should resemble this also. FRONT: 1. Logo (attached) 2. Text: Professional Prescription Formula Dispensed Only By Physicians 3. On the bottom: e 30 ml / 1 fl.oz. Made in USA BACK: All the way on the bottom - try to fit into lower 1/4th of the space: Directions: Follow the directions of your prescribing Physician Cautions: For external use only - do not ingest. Avoid contact with open wounds. Avoid getting into eyes. Make sure skin is clean and dry before applying . Discontinue use if rash or discomfort occurs. Not for use by pregnant or lactating women. The packaging is NOT child resistant. KEEP AWAY FROM CHILDREN. If accidentally ingested seek medical help immediately. _________________________ We will be using various technics while printing the boxes: uv coating, spot foil etc See several samples of the designs I liked attached. Try to stick to conservative yet fresh colors: metallic, silver, gray , blue, green.
Health
Doctors, medical professionals and their patients.

```html
<!DOCTYPE html>
<html lang="en">
<head>
<meta charset="utf-8">
<title>Veralume — Prescription Cream Box</title>
<link href="https://fonts.googleapis.com/css2?family=Montserrat:wght@300;400;500&display=swap" rel="stylesheet">
<style>
  :root {
    --backdrop-light: #eceded;
    --backdrop-dark: #c9cacb;
    --silver-light: #e4e5e6;
    --silver-mid: #b5b7b9;
    --silver-dark: #8e9092;
    --ink: #3a3b3d;
    --ink-soft: #55575a;
    --accent: #e8901f;
  }
  * { box-sizing: border-box; margin: 0; padding: 0; }
  html, body {
    width: 1200px;
    height: 901px;
    overflow: hidden;
  }
  body {
    background: radial-gradient(ellipse at 50% 40%, var(--backdrop-light) 0%, var(--backdrop-dark) 100%);
    font-family: "Montserrat", sans-serif;
    color: var(--ink);
    display: flex;
    align-items: center;
    justify-content: center;
    gap: 60px;
  }
  .panel {
    position: relative;
    width: 330px;
    height: 600px;
    background: linear-gradient(160deg, var(--silver-light) 0%, var(--silver-mid) 55%, var(--silver-dark) 100%);
    box-shadow: 0 18px 40px rgba(0,0,0,0.18);
    display: flex;
    flex-direction: column;
    align-items: center;
  }
  .panel::after {
    content: "";
    position: absolute;
    left: 0; right: 0; bottom: 0;
    height: 14px;
    background: var(--accent);
  }
  .brand {
    margin-top: 190px;
    display: flex;
    align-items: center;
    gap: 10px;
  }
  .brand-mark {
    width: 10px;
    height: 10px;
    background: var(--accent);
  }
  .brand-name {
    font-weight: 300;
    font-size: 34px;
    letter-spacing: 6px;
    text-transform: uppercase;
    color: var(--ink);
  }
  .tagline {
    margin-top: 90px;
    width: 220px;
    text-align: center;
    font-size: 11px;
    font-weight: 500;
    line-height: 1.6;
    letter-spacing: 1.2px;
    text-transform: uppercase;
    color: var(--ink-soft);
  }
  .volume {
    position: absolute;
    bottom: 40px;
    left: 0; right: 0;
    display: flex;
    justify-content: space-between;
    padding: 0 28px;
    font-size: 10px;
    letter-spacing: 1px;
    color: var(--ink-soft);
  }
  .panel-back { justify-content: flex-end; }
  .directions {
    width: 270px;
    margin-bottom: 46px;
    font-size: 9px;
    line-height: 1.6;
    color: var(--ink-soft);
  }
  .directions p + p { margin-top: 8px; }
  .directions strong { font-weight: 500; color: var(--ink); }
</style>
</head>
<body>
  <section class="panel panel-front">
    <div class="brand">
      <span class="brand-mark"></span>
      <span class="brand-name">Veralume</span>
    </div>
    <p class="tagline">Professional Prescription Formula<br>Dispensed Only By Physicians</p>
    <div class="volume">
      <span>e 30 ml / 1 fl.oz.</span>
      <span>Made in USA</span>
    </div>
  </section>

  <section class="panel panel-back">
    <div class="directions">
      <p><strong>Directions:</strong> Follow the directions of your prescribing Physician.</p>
      <p><strong>Cautions:</strong> For external use only - do not ingest. Avoid contact with open wounds. Avoid getting into eyes. Make sure skin is clean and dry before applying. Discontinue use if rash or discomfort occurs. Not for use by pregnant or lactating women. The packaging is NOT child resistant. KEEP AWAY FROM CHILDREN. If accidentally ingested seek medical help immediately.</p>
    </div>
  </section>
</body>
</html>
```